Rollvane Supply .com

This website is simple!!!
Landing page background image should capture the customers attention!!! We will provide a image as a example of what we like. The purpose for this website is to provide customers with a clean easy way to request a quote for industrial casters and wheels by OEM’s as well as maintenance departments worldwide. Please see if you can follow our thought process below.
Customer comes to website, they are invited to Request a Quote by providing us with Manufacturer Name, Manufacturers Part # and quantity needed.
If this is not known the customer will complete will WP conversation format form answering about 10 questions
Or
Look up the part number in one of the 8 to 12 catalogs located in the Pagewhirl Deck format on our catalog page, or equal plug in .
When the client request a quote a account page will pop up request The following:
Clients first and last name
Email address
And optional questions
Company name and best contact number.
Once this is complete customer will hit SUBMIT.
The customers request will be in system. A email will be sent to Customer service notifying us the Quote Request has been made.
We will then build a quote for the customer with a good, better and best options. Customers Request a Quote submission may have more than one caster or wheel requested at a time, so website must allow this.
When the customer comes back into website there email address will come up as the account name and request a password be made for them. This will allow them to store quotes in their account for future needs. If quote is older than 30 day the system will trigger a button at the bottom of the quote for resubmit Request for updated quote.
Once customer reviews quote the quote can be Converted to order within the website.
Once Converted the system will send us a email and order will be processed.
We will need a Chat program that will text to CS the questions.
You will need to have high quality graphic design skills on your team.
We have found 2 plugins that would work nicely with our new website Pagewhirl decks to showcase our catalogs for customers to research and QuillKit conversation forms to complete request for quote form.
Just Ideas:
Very very ghosted caster blueprint in white background but very very ghosted or the icon just idea
We have never had a font used we like
Grayscale every except for rubber on wheels and logo icon
Website should have hamburger menu on left
Website should hav responsive deign
Account head on right side
Has anyone read the brief from top to bottom and the updates, I’m seeing a lot of duplicates of the website I posted in images I want a clean website With lite backgrand with the poly being definite colors on each wheel I added a green yellow and red image has anyone looked at that Just a question?
Went on vacation/holiday

```html
<!DOCTYPE html>
<html lang="en">
<head>
<meta charset="utf-8">
<title>Rollvane Supply .com</title>
<link rel="stylesheet" href="https://fonts.googleapis.com/css2?family=Poppins:wght@400;500;600&display=swap">
<style>
  :root {
    --page-bg: #eef1f8;
    --ink-navy: #263f8f;
    --ink-deep: #1f3678;
    --accent-cyan: #6cf3f6;
    --hero-top: #6ff6f8;
    --hero-mid: #3aa7d3;
    --hero-bottom: #253f8e;
    --bullet: #5fe3ef;
    --white: #ffffff;
  }
  * { margin: 0; padding: 0; box-sizing: border-box; }
  html, body { width: 1200px; height: 710px; overflow: hidden; }
  body {
    background: var(--page-bg);
    font-family: "Poppins", sans-serif;
    color: var(--ink-navy);
    position: relative;
  }
  .menu-toggle {
    position: absolute; left: 16px; top: 18px;
    width: 28px; height: 22px;
  }
  .account-icon { position: absolute; right: 14px; top: 16px; width: 22px; height: 24px; }
  .hero-panel { position: absolute; left: 0; top: 0; width: 1200px; height: 620px; }
  .brand {
    position: absolute; left: 68px; top: 84px;
    display: flex; align-items: center; gap: 12px;
  }
  .brand-dot { width: 52px; height: 52px; border-radius: 50%; background: var(--ink-navy); }
  .brand-name { font-size: 30px; font-weight: 600; color: var(--ink-navy); line-height: 1; }
  .headline { position: absolute; left: 68px; top: 250px; }
  .headline span { display: block; font-size: 51px; line-height: 53px; color: var(--ink-navy); font-weight: 400; }
  .headline .lead { font-weight: 600; }
  .headline .line-2 { padding-left: 46px; }
  .headline .line-3 { padding-left: 71px; }
  .steps {
    position: absolute; left: 114px; top: 428px;
    list-style: none; font-size: 17.5px; line-height: 21.5px; color: var(--ink-navy);
  }
  .steps li { position: relative; padding-left: 17px; }
  .steps li::before {
    content: ""; position: absolute; left: 0; top: 7px;
    border-left: 6px solid var(--bullet);
    border-top: 4px solid transparent; border-bottom: 4px solid transparent;
  }
  .btn {
    position: absolute; top: 539px; height: 36px; width: 125px;
    border-radius: 18px; font-size: 13px; font-family: "Poppins", sans-serif;
    display: flex; align-items: center; justify-content: center; border: none;
  }
  .btn-quote { left: 90px; background: var(--accent-cyan); color: var(--ink-deep); }
  .btn-catalog { left: 268px; background: var(--ink-navy); color: var(--white); }
</style>
</head>
<body>
  <svg class="hero-panel" viewBox="0 0 1200 620" aria-hidden="true">
    <defs>
      <linearGradient id="heroFill" x1="0" y1="0" x2="0.75" y2="1">
        <stop offset="0" stop-color="var(--hero-top)"/>
        <stop offset="0.45" stop-color="var(--hero-mid)"/>
        <stop offset="1" stop-color="var(--hero-bottom)"/>
      </linearGradient>
    </defs>
    <path d="M565 0 L1200 0 L1200 600 L790 600 Q740 600 712 560 L500 200 Q488 160 510 125 Z" fill="url(#heroFill)"/>
  </svg>

  <svg role="img" aria-label="Photo of heavy-duty swivel casters and polyurethane wheels over a faint blueprint" style="position:absolute;left:660px;top:60px;width:460px;height:480px" viewBox="0 0 460 480">
    <defs>
      <radialGradient id="productFill" cx="0.5" cy="0.5" r="0.55">
        <stop offset="0" stop-color="#2a3f6e" stop-opacity="0.55"/>
        <stop offset="1" stop-color="#2a3f6e" stop-opacity="0"/>
      </radialGradient>
    </defs>
    <rect width="460" height="480" fill="url(#productFill)"/>
  </svg>

  <svg class="menu-toggle" viewBox="0 0 28 22" aria-label="Menu" role="img">
    <rect x="0" y="3" width="28" height="2.6" rx="1.3" fill="#8a94a6"/>
    <rect x="0" y="10" width="28" height="2.6" rx="1.3" fill="#8a94a6"/>
    <rect x="0" y="17" width="28" height="2.6" rx="1.3" fill="#8a94a6"/>
  </svg>

  <svg class="account-icon" viewBox="0 0 22 24" aria-label="Account" role="img">
    <circle cx="11" cy="7" r="5" fill="#ffffff"/>
    <path d="M2 23 Q2 13 11 13 Q20 13 20 23 Z" fill="#ffffff"/>
  </svg>

  <div class="brand">
    <span class="brand-dot"></span>
    <span class="brand-name">Rollvane Supply .com</span>
  </div>

  <h1 class="headline">
    <span class="lead">#1 Solutions</span>
    <span class="line-2">for all your</span>
    <span class="line-3">Applications</span>
  </h1>

  <ul class="steps">
    <li>Request a quote</li>
    <li>Received a quote</li>
    <li>Convert a quote to order</li>
  </ul>

  <button class="btn btn-quote">Request Quote</button>
  <button class="btn btn-catalog">Open Catalog</button>
</body>
</html>
```